Word Page Templates x 5

1 x Letterhead Template with Header and Footer able to be printed to paper and pdf with non blurry resolution
- File attached looks ok on computer screen but does not print the same
- We are wanting it to print like it looks on the screen
- We are wanting it to print not fuzzy in resolution
- We are wanting the banner to be on the absolute edge of the page like it is on the computer screen
- We are needing to print this to paper and pdf with perfect resolution and colour

Please can someone help us!!

I have provided the logo files in our posession. If better resolutions are required please let us know.

We are also wanting 4 simple page templates to be setup in Landscape and Portrait orientation as well once we are happy with the letterhead that is provided samples have been provided
Updates

Hi all I have the vector files available now along with a Colour profile

Requirements
Must have
• Clear when printed on A4 Paper
Should not have
• Blurry images, Colour must be correct (same as Logo) - Please reference our website if need be ..... vornal.com.au

```html
<!DOCTYPE html>
<html lang="en">
<head>
<meta charset="utf-8">
<title>Vornal Pavement Services – Letterhead</title>
<link rel="stylesheet" href="https://fonts.googleapis.com/css2?family=Open+Sans:wght@400;600;700;800&display=swap">
<style>
  :root {
    --backdrop: #1d2228;
    --paper: #ffffff;
    --navy: #1f3c84;
    --green: #1b7a3e;
    --rule-green: #1d6b35;
    --grey: #8a8a8a;
    --band-start: #2f7a45;
    --band-mid: #3b5a74;
    --band-end: #4a3d78;
    --badge-tone: #e4e8ef;
  }
  * { box-sizing: border-box; margin: 0; padding: 0; }
  html, body {
    width: 1200px; height: 1200px; overflow: hidden;
    background: var(--backdrop);
    font-family: "Open Sans", Arial, sans-serif;
  }
  .letterhead {
    position: absolute; left: 211px; top: 50px;
    width: 778px; height: 1100px;
    background: var(--paper);
  }
  .edge-band {
    position: absolute; left: 0; width: 100%; height: 30px;
    background: linear-gradient(90deg, var(--band-start), var(--band-mid) 50%, var(--band-end));
  }
  .edge-band.top { top: 0; }
  .edge-band.bottom { bottom: 0; }

  .brand-name {
    position: absolute; display: flex; align-items: center; gap: 10px;
    color: var(--navy); font-weight: 800; letter-spacing: 2px; line-height: 1;
  }
  .brand-name .mark { background: var(--green); display: block; }
  .header-brand { left: 26px; top: 62px; font-size: 60px; }
  .header-brand .mark { width: 30px; height: 30px; }
  .footer-brand { left: 563px; top: 990px; font-size: 40px; }
  .footer-brand .mark { width: 20px; height: 20px; }

  .contact-list {
    position: absolute; left: 531px; top: 62px;
    list-style: none; font-size: 11px; font-weight: 700; color: var(--navy);
  }
  .contact-list li { height: 20px; line-height: 20px; display: flex; }
  .contact-list .label { color: var(--green); width: 24px; }

  .rule { position: absolute; height: 4px; }
  .rule.navy { left: 26px; top: 927px; width: 427px; background: var(--navy); }
  .rule.green { left: 559px; top: 925px; width: 192px; background: var(--rule-green); }

  .affiliation-title {
    position: absolute; left: 26px; top: 943px;
    font-size: 13px; font-weight: 600; letter-spacing: 1px; color: var(--navy);
  }
  .badges { position: absolute; left: 26px; top: 982px; display: flex; align-items: center; gap: 10px; }
  .badge { background: var(--badge-tone); border-radius: 4px; height: 60px; }
  .badge.w1 { width: 160px; }
  .badge.w2 { width: 95px; }
  .badge.w3 { width: 66px; }
  .badge.w4 { width: 68px; }
</style>
</head>
<body>
  <main class="letterhead">
    <div class="edge-band top" role="img" aria-label="Green to purple chevron stripe band along the top edge"></div>

    <div class="brand-name header-brand"><span class="mark"></span>VORNAL</div>

    <ul class="contact-list">
      <li><span class="label">A:</span>PO Box 2318, Carrow Qld 4290</li>
      <li><span class="label">P:</span>07 5500 1234</li>
      <li><span class="label">E:</span>admin@vornal.com.au</li>
      <li><span class="label">W:</span>www.vornal.com.au</li>
    </ul>

    <div class="rule navy"></div>
    <div class="rule green"></div>

    <p class="affiliation-title">VORNAL PAVEMENT SERVICES ARE PROUDLY AFFILIATED WITH</p>
    <div class="badges">
      <div class="badge w1" role="img" aria-label="Affiliate badge"></div>
      <div class="badge w2" role="img" aria-label="Affiliate badge"></div>
      <div class="badge w3" role="img" aria-label="Affiliate badge"></div>
      <div class="badge w4" role="img" aria-label="Affiliate badge"></div>
    </div>

    <div class="brand-name footer-brand"><span class="mark"></span>VORNAL</div>

    <div class="edge-band bottom" role="img" aria-label="Green to purple chevron stripe band along the bottom edge"></div>
  </main>
</body>
</html>
```